Design a modern, classy & professional business card for an online real estate agency, specializing in medium-luxury properties in Thailand and later in Singapore and UK.

Possible design ideas so far: (not essential)

- curved corner(s) to the card, white on front & turquoise on back or visa versa.

- front of card - clear and simple, company name in metallic grey/monochrome, logo graphic & company name on front in spot UV or embossed/debossed effect.

- back of card - large, close-cropped, 'ghost' patterns of the C-shaped curves of logo, or company name repeated on back of card in spot UV.

Target Market(s)

- young to middle-aged professionals mainly (but ideally should design should suit all)

- UK, US,EU,AUS & ASIAN mainly (but ideally should design should suit all countries)

Industry/Entity Type

Real Estate

Requirements
Must have
• THEME:
- Luxurious & Modern
- Clean & striking
- Unique & creative

INFO:
- Logo & company name on front
- Contact details on back:

Tobias Lindqvar
Managing Director

www.velmoraestates.example
www.velmoraestates-uk.example

Tel: 084-273-6190
email: tobias@velmoraestates.example

(contact details can be displayed in any order as suites design.)

Nice to have
• - curved corner(s) to the card, white on front & turquoise on back or visa versa.

Should not have
• - No generic images of properties, palm trees/coconut trees etc.

- No other other bold colors, except for main turquoise, grey, metallic white & black theme.

- No obvious business card templates

```html
<!DOCTYPE html>
<html lang="en">
<head>
<meta charset="utf-8">
<title>Velmora Estates – Business Card</title>
<link rel="stylesheet" href="https://fonts.googleapis.com/css2?family=Open+Sans:wght@400;600&display=swap">
<style>
  :root {
    --page-bg: #e9eaea;
    --turquoise: #4cc3c0;
    --turquoise-deep: #36a9a6;
    --turquoise-light: #8fe3df;
    --card-white: #ffffff;
    --ink: #4a4d50;
    --ink-soft: #6d7073;
    --rule: #4cc3c0;
  }
  * { box-sizing: border-box; margin: 0; padding: 0; }
  html, body {
    width: 900px;
    height: 1200px;
    overflow: hidden;
    background: var(--page-bg);
    font-family: "Open Sans", Arial, sans-serif;
  }
  .canvas {
    position: relative;
    width: 900px;
    height: 1200px;
    display: flex;
    flex-direction: column;
    align-items: center;
    justify-content: center;
    gap: 90px;
  }
  .card {
    position: relative;
    width: 640px;
    height: 366px;
    border-radius: 36px;
    overflow: hidden;
  }
  /* Turquoise side */
  .card--pattern {
    background: var(--turquoise);
  }
  .card__pattern-field {
    position: absolute;
    inset: 0;
    background:
      radial-gradient(ellipse at 20% 10%, var(--turquoise-light) 0%, transparent 55%),
      radial-gradient(ellipse at 85% 95%, var(--turquoise-light) 0%, transparent 50%),
      linear-gradient(135deg, var(--turquoise) 0%, var(--turquoise-deep) 100%);
    opacity: 0.95;
  }
  .card__brand-mark {
    position: absolute;
    inset: 0;
    display: flex;
    align-items: center;
    justify-content: center;
    color: var(--card-white);
    font-size: 46px;
    font-weight: 600;
    letter-spacing: 1px;
  }
  /* White side */
  .card--contact {
    background: var(--card-white);
    box-shadow: 0 2px 0 rgba(0,0,0,0.04);
    display: flex;
    flex-direction: column;
    align-items: center;
    padding-top: 38px;
    color: var(--ink);
    text-align: center;
  }
  .brand {
    display: flex;
    align-items: center;
    gap: 14px;
  }
  .brand__square {
    width: 62px;
    height: 62px;
    background: var(--turquoise);
  }
  .brand__name {
    font-size: 40px;
    font-weight: 400;
    color: var(--ink-soft);
    line-height: 1;
  }
  .person {
    margin-top: 38px;
  }
  .person__name {
    font-size: 19px;
    font-weight: 600;
    color: var(--ink);
  }
  .person__title {
    font-size: 12px;
    color: var(--ink-soft);
    margin-top: 2px;
  }
  .person__rule {
    width: 96px;
    height: 1.5px;
    background: var(--rule);
    margin: 8px auto 0;
  }
  .contact {
    margin-top: 12px;
    font-size: 13.5px;
    line-height: 1.6;
    color: var(--ink);
  }
  .web {
    margin-top: 10px;
    font-size: 13.5px;
    line-height: 1.55;
    color: var(--ink);
  }
  .social {
    margin-top: 14px;
    display: flex;
    gap: 10px;
  }
  .social__chip {
    width: 18px;
    height: 18px;
    background: var(--turquoise-deep);
  }
</style>
</head>
<body>
<main class="canvas">
  <section class="card card--pattern">
    <div class="card__pattern-field" role="img" aria-label="Ghosted repeating pattern of interlocking C-shaped curves in spot UV on turquoise"></div>
    <div class="card__brand-mark">Velmora Estates</div>
  </section>

  <section class="card card--contact">
    <div class="brand">
      <span class="brand__square"></span>
      <span class="brand__name">Velmora Estates</span>
    </div>
    <div class="person">
      <p class="person__name">Tobias Lindqvar</p>
      <p class="person__title">Managing Director</p>
      <div class="person__rule"></div>
    </div>
    <div class="contact">
      <p>084-273-6190</p>
      <p>tobias@velmoraestates.example</p>
    </div>
    <div class="web">
      <p>www.velmoraestates.example</p>
      <p>www.velmoraestates-uk.example</p>
    </div>
    <div class="social" aria-label="Social profiles">
      <span class="social__chip"></span>
      <span class="social__chip"></span>
      <span class="social__chip"></span>
    </div>
  </section>
</main>
</body>
</html>
```